Revamp Page To Have A Sleek, Futuristic, Artificial Intelligence type of feel to it

I have become a white label reseller of www.brontavise.com and have permission to use all their content, etc for my website.

Do not use the same images please...please find our own and also reformat the website so it doesnt look exact...it should look totally different but with all the same content...but different imagery throughout and of course use my logo...see attached.

Target Market(s)

B2B

Industry/Entity Type

marketing automations, chatbots, crm, email and sms campaigns, drip campaigns.

Coding

Coded - Design and coding required

Requirements
Must have
• use different images than what is provided on the current page. This is a full redesign using all the same content/text/wording but not the same imagery...
Nice to have
• I would like the website to have a futuristic, AI, Automations FEEL TO IT...so it seems futuristic and here to stay
Should not have

```html
<!DOCTYPE html>
<html lang="en">
<head>
<meta charset="utf-8">
<title>Vantrix Automations – All-In-One Sales &amp; Marketing Platform</title>
<link href="https://fonts.googleapis.com/css2?family=Poppins:ital,wght@0,400;0,500;0,600;0,700;1,500&display=swap" rel="stylesheet">
<style>
:root{
  --navy:#0b1f4f;
  --hero-deep:#1a0b4a;
  --hero-mid:#3a14a8;
  --violet:#5b3cf5;
  --violet-soft:#7e64ff;
  --blue:#2f8df5;
  --ink:#111;
  --white:#fff;
  --grey:#e4e4ea;
  --muted:#444;
}
*{box-sizing:border-box;margin:0;padding:0}
html,body{width:1200px;height:4298px;overflow:hidden}
body{font-family:'Poppins',sans-serif;color:var(--ink);background:var(--white);position:relative}
.abs{position:absolute}

/* hero */
.hero{left:0;top:0;width:1200px;height:722px;background:radial-gradient(ellipse at 80% 40%,#5a24d6 0%,var(--hero-mid) 35%,var(--hero-deep) 100%)}
.logo-badge{background:var(--white);border-radius:12px;display:flex;flex-direction:column;align-items:center;justify-content:center;box-shadow:0 3px 8px rgba(0,0,0,.25)}
.logo-badge .mark{width:22px;height:14px;background:var(--violet);border-radius:3px}
.logo-badge .name{font-size:7px;font-weight:600;color:var(--navy);margin-top:2px}
.nav a{position:absolute;top:31px;font-size:13px;color:var(--white);text-decoration:none}
.btn-contact{left:1001px;top:20px;width:110px;height:33px;border:1.5px solid var(--violet-soft);background:var(--violet);border-radius:6px;color:var(--white);font-size:13px;display:flex;align-items:center;justify-content:center}
.hero-title{left:88px;top:258px;color:var(--white);font-size:27px;font-weight:500;line-height:37px}
.hero-title em{font-weight:500}
.btn-blue{background:var(--blue);color:var(--white);border-radius:5px;display:flex;align-items:center;justify-content:center;font-size:12px;box-shadow:0 4px 10px rgba(0,0,0,.2)}
.hero-visual{left:709px;top:192px;width:402px;height:308px;border-radius:30px;background:radial-gradient(ellipse at center,#8a5cff 0%,#4d2ad0 55%,rgba(58,20,168,0) 80%)}

/* about band */
.navy-band{left:0;top:721px;width:1200px;height:1124px;background:var(--navy)}
.about-card{left:174px;top:634px;width:1026px;height:579px;background:var(--violet);border-radius:14px 0 0 14px}
.about-title{left:250px;top:750px;color:var(--white);font-size:24px;line-height:31px}
.about-text{left:250px;top:840px;color:var(--white);font-size:16px;line-height:22.5px}
.btn-dark{background:var(--ink);color:var(--white);border-radius:4px;font-size:11px;display:flex;align-items:center;gap:24px;padding-left:20px;box-shadow:3px 3px 0 rgba(0,0,0,.35)}
.video{left:721px;top:698px;width:391px;height:424px;background:var(--grey);border-radius:14px;overflow:hidden}
.video .tab{position:absolute;left:0;top:0;width:160px;height:31px;background:var(--ink);color:var(--white);font-size:12px;display:flex;align-items:center;justify-content:center;border-radius:14px 0 10px 0}
.stats{left:250px;top:1033px;width:775px;height:97px;background:var(--white);border-radius:12px;box-shadow:6px 6px 0 rgba(0,0,0,.25);display:flex;align-items:center;justify-content:space-around}
.stat{text-align:center;font-size:15px;line-height:20px;font-weight:500;width:170px}
.stat b{font-weight:600;display:block}
.stat-sep{width:1.5px;height:22px;background:var(--ink)}

/* questions */
.portrait{left:112px;top:1319px;width:457px;height:407px;border-radius:10px;background:linear-gradient(90deg,#2a2e33 0%,#3b4046 45%,#cfd2d6 46%,#b9bcc1 100%)}
.question{left:659px;color:var(--white);font-size:23px;line-height:30px}
.btn-outline{left:659px;top:1676px;width:334px;height:50px;border:1.5px solid var(--white);border-radius:8px;color:var(--white);font-size:14px;display:flex;align-items:center;justify-content:space-between;padding:0 40px 0 30px}

/* clients */
.pill{background:var(--white);border-radius:22px;box-shadow:0 3px 8px rgba(0,0,0,.2);display:flex;align-items:center;justify-content:center;font-weight:600;font-size:21px}
.client{top:2008px;height:40px;display:flex;align-items:center;gap:8px;font-size:28px;font-weight:600;color:var(--navy)}
.client .dot{width:22px;height:22px;border-radius:50%;background:currentColor}
.badge{left:188px;top:2000px;width:112px;height:56px;border-radius:6px;background:#bcd6ee}

/* testimonials */
.navy-strip{left:0;top:2490px;width:1200px;height:602px;background:var(--navy)}
.testi-card{left:90px;top:2121px;width:1020px;height:778px;background:var(--violet)}
.tile{width:257px;height:170px;border-radius:10px;box-shadow:0 4px 10px rgba(0,0,0,.2);display:flex;align-items:center;justify-content:center}
.r1{background:var(--white)}
.r2{background:linear-gradient(180deg,#fff 40%,#c9bdfd 100%)}
.r3{background:linear-gradient(180deg,#b3a3fc 0%,#8d74ff 100%)}

/* pricing */
.plan{background:var(--white);border-radius:8px;box-shadow:0 20px 30px rgba(0,0,0,.18);text-align:center}
.plan h3{font-size:16px;font-weight:500;line-height:20px;margin-top:28px}
.plan .price{font-size:34px;font-weight:600;margin-top:28px}
.plan .price small{font-size:14px;font-weight:400;color:var(--muted)}
.feat{display:flex;gap:14px;text-align:left;font-size:10px;line-height:22px;color:var(--ink);margin:0 0 18px 34px}
.feat b{font-weight:600}
.feat svg{flex:0 0 20px;margin-top:2px}
.plan .btn-blue{position:absolute;height:40px}

/* footer */
.footer{left:0;top:3899px;width:1200px;height:399px;background:var(--navy);color:var(--white)}
.fcol{font-size:11px;line-height:20px}
.fcol h4{font-size:10px;font-weight:600}
.rule{left:210px;top:4233px;width:735px;height:2px;background:var(--white)}
</style>
</head>
<body>

<!-- hero -->
<section class="abs hero">
  <div class="abs logo-badge" style="left:88px;top:28px;width:120px;height:34px"><span class="mark"></span><span class="name">Vantrix Automations</span></div>
  <nav class="nav">
    <a style="left:606px">Home</a><a style="left:683px">Services</a><a style="left:773px">About</a><a style="left:851px">Projects</a><a style="left:940px;top:29px">Blog</a>
  </nav>
  <div class="abs btn-contact">Contact us</div>
  <h1 class="abs hero-title">We Help <em>Agencies &amp; Marketers</em> Thrive<br>With Our All-In-One Sales &amp; Marketing Platform<br>[ FOR AGENCIES, BY AN AGENCY ]</h1>
  <div class="abs btn-blue" style="left:87px;top:404px;width:270px;height:37px">Start Your 14 Day Free Trial Today!</div>
  <div class="abs hero-visual" role="img" aria-label="Laptop showing a glowing analytics dashboard"></div>
</section>

<!-- about -->
<div class="abs navy-band"></div>
<section class="abs about-card"></section>
<h2 class="abs about-title" style="font-weight:400">We're In The Business<br>Of Helping You Grow Your Agency</h2>
<p class="abs about-text">Brontavise is the first-ever all-in-one platform<br>that will give you the tools,<br>support and resources you need to<br>succeed with your agency.</p>
<div class="abs btn-dark" style="left:250px;top:953px;width:146px;height:27px">Know More
  <svg width="18" height="10" viewBox="0 0 18 10"><path d="M0 5h16M12 1l4 4-4 4" stroke="#fff" stroke-width="1.4" fill="none"/></svg></div>
<div class="abs video">
  <div class="tab">Watch Demo</div>
  <svg class="abs" style="left:167px;top:184px" width="56" height="56" viewBox="0 0 56 56"><circle cx="28" cy="28" r="28" fill="#000"/><path d="M22 17l17 11-17 11z" fill="#fff"/></svg>
</div>
<div class="abs stats">
  <div class="stat">15000+<b>Agencies</b></div><span class="stat-sep"></span>
  <div class="stat">523K+<b>Businesses</b></div><span class="stat-sep"></span>
  <div class="stat">622.3M+<b>Leads</b></div><span class="stat-sep"></span>
  <div class="stat">9.2B+<b>Conversations</b></div>
</div>

<!-- questions -->
<div class="abs portrait" role="img" aria-label="Photo of a business coach speaking in a studio"></div>
<p class="abs question" style="top:1333px">DO YOU WANT TO KEEP YOUR<br>CLIENTS LONGER?</p>
<p class="abs question" style="top:1453px">DO YOU WANT TO SCALE<br>YOUR BUSINESS?</p>
<p class="abs question" style="top:1573px">DO YOU WANT MORE<br>CUSTOMERS?</p>
<div class="abs btn-outline">We have Got you Covered
  <svg width="26" height="20" viewBox="0 0 26 20"><path d="M2 2l8 8-8 8M13 2l8 8-8 8" stroke="#fff" stroke-width="1.6" fill="none"/></svg></div>

<!-- clients -->
<div class="abs pill" style="left:494px;top:1899px;width:210px;height:44px">Our Clients</div>
<div class="abs badge" role="img" aria-label="Compliance certificate badge"></div>
<div class="abs client" style="left:405px;color:#e0352b"><span class="dot"></span>Postvane</div>
<div class="abs client" style="left:656px;color:#1b3a70"><span class="dot" style="border-radius:2px"></span>Mailstrand</div>
<div class="abs client" style="left:905px;color:#e43a4b"><span class="dot"></span>Callora</div>

<!-- testimonials -->
<div class="abs navy-strip"></div>
<section class="abs testi-card"></section>
<div class="abs pill" style="left:494px;top:2151px;width:214px;height:45px;color:var(--navy)">What they Say</div>
<svg width="0" height="0" style="position:absolute"><defs><g id="play"><circle cx="15" cy="15" r="15" fill="#000"/><path d="M11 8.5l11 6.5-11 6.5z" fill="#fff"/></g></defs></svg>
<div class="abs tile r1" style="left:164px;top:2228px"><svg width="30" height="30"><use href="#play"/></svg></div>
<div class="abs tile r1" style="left:472px;top:2228px"><svg width="30" height="30"><use href="#play"/></svg></div>
<div class="abs tile r1" style="left:779px;top:2228px"><svg width="30" height="30"><use href="#play"/></svg></div>
<div class="abs tile r2" style="left:164px;top:2457px"><svg width="30" height="30"><use href="#play"/></svg></div>
<div class="abs tile r2" style="left:472px;top:2457px"><svg width="30" height="30"><use href="#play"/></svg></div>
<div class="abs tile r2" style="left:779px;top:2457px"><svg width="30" height="30"><use href="#play"/></svg></div>
<div class="abs tile r3" style="left:164px;top:2687px"><svg width="30" height="30"><use href="#play"/></svg></div>
<div class="abs tile r3" style="left:472px;top:2687px"><svg width="30" height="30"><use href="#play"/></svg></div>
<div class="abs tile r3" style="left:779px;top:2687px"><svg width="30" height="30"><use href="#play"/></svg></div>
<div class="abs btn-dark" style="left:527px;top:2844px;width:147px;height:27px">Know More
  <svg width="18" height="10" viewBox="0 0 18 10"><path d="M0 5h16M12 1l4 4-4 4" stroke="#fff" stroke-width="1.4" fill="none"/></svg></div>

<!-- pricing -->
<div class="abs pill" style="left:494px;top:3146px;width:210px;height:44px">Pricing</div>
<svg width="0" height="0" style="position:absolute"><defs><g id="tick"><circle cx="10" cy="10" r="8" fill="none" stroke="#222" stroke-width="1.4"/><path d="M6 10l3 3 9-9" stroke="#222" stroke-width="1.6" fill="none"/></g></defs></svg>

<article class="abs plan" style="left:174px;top:3288px;width:330px;height:484px">
  <h3>Agency Starter<br>Account</h3>
  <p class="price">$97<small>/mon</small></p>
  <div style="margin-top:18px">
    <div class="feat"><svg width="20" height="20"><use href="#tick"/></svg><span><b>CALLORA</b> - JUST ENTER YOUR OWN KEYS<br>ENABLE 2-WAY TEXTING</span></div>
    <div class="feat"><svg width="20" height="20"><use href="#tick"/></svg><span><b>POSTVANE</b> - JUST ENTER YOUR OWN KEYS<br>FOR UNLIMITED SENDING</span></div>
    <div class="feat"><svg width="20" height="20"><use href="#tick"/></svg><span><b>SINGLE ACCOUNT</b> - SETUP 1 CLIENT TO<br>USE FOR YOUR OWN AGENCY</span></div>
  </div>
  <div class="btn-blue" style="left:26px;top:398px;width:270px">Start Your 14 Day Free Trial Today!</div>
</article>

<article class="abs plan" style="left:706px;top:3288px;width:319px;height:484px">
  <h3>White Label Mobile App +<br>Custom Flow Upgrade</h3>
  <p class="price">$497<small>/mon</small></p>
  <div style="margin-top:18px">
    <div class="feat" style="margin-left:80px"><span><b>MOBILE APP</b> - WE WILL CREATE A<br>CUSTOMIZED MOBILE APP SO THAT YOU<br>CAN BE FULLY BRANDED</span></div>
    <div class="feat" style="margin-left:80px"><span><b>LINKFLOW</b> - WE WILL CREATE A CUSTOM<br>FLOW JUST FOR YOUR BRAND</span></div>
    <div class="feat" style="margin-left:80px"><span><b>REQUIREMENTS</b> - THIS UPGRADE<br>REQUIRES THE AGENCY UNLIMITED<br>ACCOUNT.</span></div>
  </div>
  <div class="btn-blue" style="left:30px;top:396px;width:270px">Start Your 14 Day Free Trial Today!</div>
</article>

<article class="abs plan" style="left:416px;top:3230px;width:367px;height:642px;z-index:2">
  <h3 style="margin-top:34px">Agency Unlimited Account</h3>
  <p class="price" style="margin-top:30px">$297<small>/mon</small></p>
  <div style="margin-top:28px">
    <div class="feat"><svg width="20" height="20"><use href="#tick"/></svg><span><b>EVERYTHING IN AGENCY STARTER</b></span></div>
    <div class="feat"><svg width="20" height="20"><use href="#tick"/></svg><span><b>UNLIMITED SUB ACCOUNTS</b> - CREATE<br>AS MANY ACCOUNTS AS YOU'D LIKE FOR<br>YOUR CLIENTS OR OTHER BUSINESSES</span></div>
    <div class="feat"><svg width="20" height="20"><use href="#tick"/></svg><span><b>BRANDED DESKTOP APP</b> - OUT OF THE<br>BOX, YOU'LL HAVE THE ABILITY TO USE<br>YOUR OWN DOMAIN AND CUSTOMIZE<br>THE LOOK AND FEEL OF THE PLATFORM</span></div>
  </div>
  <div class="btn-blue" style="left:48px;top:508px;width:272px">Start Your 14 Day Free Trial Today!</div>
</article>

<!-- footer -->
<footer class="abs footer">
  <div class="abs logo-badge" style="left:174px;top:50px;width:130px;height:50px"><span class="mark"></span><span class="name" style="font-size:9px">Vantrix Automations</span></div>
  <div class="abs fcol" style="left:174px;top:140px">
    <h4>CONTACT US</h4>
    <p>Corporate HQ<br>218 Meridian Park Ave.<br>Suite 410<br>Aurelton, Texas 75990</p>
    <p style="margin-top:20px"><b>Toll Free:</b> (888) 555-0148</p>
  </div>
  <div class="abs fcol" style="left:424px;top:74px"><h4>LEGAL</h4><p>Privacy Policy<br>Terms of Service<br>GDPR Compliance</p></div>
  <div class="abs fcol" style="left:424px;top:198px"><h4>LEGAL</h4><p>Privacy Policy<br>Terms of Service<br>GDPR Compliance</p></div>
  <div class="abs fcol" style="left:641px;top:74px"><h4>AFFILIATES</h4><p>Affiliate Login<br>Become an Affiliate<br>Affiliate Agreement</p></div>
  <div class="abs fcol" style="left:641px;top:198px"><h4>AFFILIATES</h4><p>Affiliate Login<br>Become an Affiliate<br>Affiliate Agreement</p></div>
  <div class="abs fcol" style="left:863px;top:64px"><h4>FEATURES</h4><p>Insights<br>Dashboard<br>Outbound Calling<br>Appointment Automation<br>Reputation Management<br>Unified Messaging<br>Lead Management<br>Easy Integration<br>Mobile App</p></div>
  <p class="abs" style="left:0;width:1200px;top:362px;text-align:center;font-size:10px">© 2021 Brontavise, LLC. | All Rights Reserved</p>
</footer>
<div class="abs rule"></div>

</body>
</html>
```